Pagemill Design Project

We are looking for a new design for our website - and need your help to make it great.

Our current website is here: http://www.morvik.com: It has way too much information on it and it lacks a clear focus.

You can download the current design approach here: http://qx.zp/kRbn52dwya

It is a layered PSD file with the various approved images for the different sections. We have also uploaded images to the project which you can use.

Please use these section images in your designs with improvement suggestions as per below.

What we still need:

Header: We are not entirely sure about the header yet - variations for this would be great.

Colour scheme: We are not sure about the colour scheme yet: if you have better ideas, please present them. May be less colours, or muted colours ?

Improvements required to section images:

Full design Freedom: The monitor with t-shirts is fine, the middle screen should be a gallery of modern watches (image provided or you can create a better one) and the fruits - image provided (see attached image Morvik_site_development_blue-header)

Many product types: really only the text in the bubbles needs some improvements

Main Website Font:

The font in the supplied PSD file is a Quillet web font called Open Sans http://www.quillet.com/fonts/specimen/Open+Sans

This font is quite nice, but not so easy to read on some backgrounds. It can be replaced with a stronger font which does not look too heavy or playful.

Font for: "Click on any T-Shirt to see how it works": http://www.brindlework.com.au/type/sketch.html. If you can think of a nicer handwritten code you are welcome - I am happy with this one.

we are also lacking the additional page designs - content, blog, contact, pricing and so on.

We are quite far down the track with this design - only participate if you think you can create a genuinely better and stronger approach.

Target Market(s)

Designers and small business owners

Industry/Entity Type

Quillet

Requirements
Must have
• Home page (improvement of current approach)
Note that text and section images are approved apart from those listed above - so only create others if you can do genuinely better
content page
contact page
A better footer
blog design
pricing page
Nice to have
• anything else you can come up with to make the site look more appealing and professional.

We only need designs - and layered psd files - programming will be a separate task
Should not have
• Photos which are TOO stock style. We use pixvarna and lumeroz

```html
<!DOCTYPE html>
<html lang="en">
<head>
<meta charset="utf-8">
<title>Morvik – eCommerce made simple</title>
<link rel="stylesheet" href="https://fonts.googleapis.com/css2?family=Roboto+Condensed:wght@300;400;700&family=Montserrat:wght@400;600;700&display=swap">
<style>
:root{
  --blue:#1f6fb8;
  --blue-head:#2b7fc4;
  --sky-a:#1b78cc;
  --sky-b:#4ea6ea;
  --orange:#f07a22;
  --orange-dark:#d9620f;
  --ink:#3a3a3a;
  --brown:#4a3832;
  --footer:#333333;
  --footer-base:#282828;
  --footer-text:#a8a8a8;
  --footer-head:#3fa4e6;
  --white:#ffffff;
  --red-link:#d4121a;
}
*{box-sizing:border-box;margin:0;padding:0}
html,body{width:763px;height:1200px;overflow:hidden;background:var(--white)}
body{position:relative;font-family:"Montserrat",Arial,sans-serif;color:var(--ink)}

/* header */
.site-header{position:absolute;left:0;top:0;width:763px;height:63px;background:var(--white)}
.brand{position:absolute;left:90px;top:17px;font:700 22px "Montserrat",sans-serif;color:var(--blue);letter-spacing:-.5px}
.main-nav{position:absolute;top:28px;left:0;width:763px;font:700 8px "Montserrat",sans-serif;color:#6d6d6d;text-transform:uppercase}
.main-nav span{position:absolute;white-space:nowrap}
.main-nav .login{color:var(--blue)}
.main-nav .register{color:var(--orange-dark)}
.main-nav svg{vertical-align:-1px;margin-right:3px}

/* hero */
.hero{position:absolute;left:0;top:63px;width:763px;height:200px;background:linear-gradient(180deg,var(--sky-b) 0%,var(--sky-a) 100%)}
.hero-monitor{position:absolute;left:100px;top:10px;width:220px;height:186px;border-radius:6px;background:linear-gradient(180deg,#3a3a3a 0%,#6b8a3a 30%,#c9702c 60%,#d8d8d8 85%,#b9b9b9 100%)}
.hero-title{position:absolute;left:356px;top:14px;font:300 19.5px "Roboto Condensed",sans-serif;color:var(--white);white-space:nowrap}
.hero-copy{position:absolute;left:357px;top:46px;width:310px;font:400 12px/19.5px "Roboto Condensed",sans-serif;color:var(--white)}
.btn-start{position:absolute;left:356px;top:150px;width:125px;height:27px;border-radius:3px;background:linear-gradient(180deg,#ffa43a,var(--orange-dark));border:1px solid #c95e10;font:700 10px/25px "Montserrat",sans-serif;color:var(--white);text-align:center}

/* promo */
.promo{position:absolute;left:0;top:263px;width:763px;height:315px;background:linear-gradient(90deg,#f1ebe5 0%,#e6dcd2 45%,#d8c8ba 60%,#eae2da 100%)}
.promo-model{position:absolute;left:470px;top:6px;width:192px;height:309px;background:linear-gradient(180deg,#b98a66 0%,#c7763d 35%,#f3efeb 55%,#4d6a8e 85%);border-radius:70px 70px 0 0;opacity:.85}
.promo-title{position:absolute;left:95px;top:50px;font:700 28px "Roboto Condensed",sans-serif;color:var(--brown);white-space:nowrap}
.promo-title em{font-style:normal;color:var(--orange)}
.promo-copy{position:absolute;left:96px;top:117px;width:320px;font:400 12.5px/19px "Roboto Condensed",sans-serif;color:#3d3330}
.partners{position:absolute;left:91px;font:700 8.5px "Montserrat",sans-serif;color:#8f8883;white-space:nowrap}
.partners span{margin-right:10px}

/* features */
.feature-title{position:absolute;top:602px;font:400 18.5px "Roboto Condensed",sans-serif}
.feature-title.blue{left:89px;color:var(--blue-head)}
.feature-title.dark{left:440px;color:#333}
.feature-copy{position:absolute;top:633px;font:400 9.3px/14.6px "Montserrat",sans-serif;color:#333}
.magic{position:absolute;left:89px;top:694px;font:700 9px "Montserrat",sans-serif;color:#333}
.card-label{position:absolute;top:719px;width:70px;text-align:center;font:400 6.5px "Montserrat",sans-serif;color:#555}
.product-card{position:absolute;top:731px;width:70px;height:108px;border:1px solid #ddd;border-radius:4px;background:linear-gradient(#fff,#f3f3f3);text-align:center}
.product-photo{position:absolute;left:8px;top:8px;width:52px;height:42px;border:1px solid #e5e5e5;border-radius:2px}
.product-name{position:absolute;left:0;top:55px;width:100%;font:700 8px/11px "Montserrat",sans-serif;color:var(--orange-dark)}
.buy-now{position:absolute;left:8px;top:83px;width:53px;height:14px;border:1px solid #bbb;border-radius:7px;background:linear-gradient(#fff,#ddd);font:700 6.5px/12px "Montserrat",sans-serif;color:#444}
.more-links{position:absolute;left:89px;top:852px;font:400 9.3px/14.5px "Montserrat",sans-serif;color:#333}
.more-links b{font-weight:400;color:var(--red-link)}
.video{position:absolute;left:441px;top:704px;width:232px;height:143px;background:linear-gradient(180deg,#e9e9e9 0%,#f4f4f4 55%,#3d7ab8 80%,#2d5f94 100%)}
.video-bar{position:absolute;left:0;bottom:0;width:232px;height:12px;background:#1d1d1d}
.video-play{position:absolute;left:94px;top:44px}

/* footer */
.site-footer{position:absolute;left:0;top:917px;width:763px;height:240px;background:var(--footer)}
.footer-head{position:absolute;top:22px;font:400 16px "Roboto Condensed",sans-serif;color:var(--footer-head)}
.footer-text{position:absolute;font:400 8px/14px "Montserrat",sans-serif;color:var(--footer-text)}
.field{position:absolute;left:89px;width:138px;height:19px;background:#2a2a2a;border:1px solid #262626;font:400 8px/17px "Montserrat",sans-serif;color:#8a8a8a;padding-left:6px}
.btn-submit{position:absolute;left:90px;top:144px;width:53px;height:20px;border-radius:3px;background:linear-gradient(#6a6a6a,#444);border:1px solid #222;font:700 8px/18px "Montserrat",sans-serif;color:#ddd;text-align:center}
.share{position:absolute;top:187px;height:12px;border:1px solid #bbb;border-radius:2px;background:#f4f4f4;font:700 6px/10px "Montserrat",sans-serif;color:#333;padding:0 3px}
.article-title{position:absolute;left:281px;font:700 8px/10px "Montserrat",sans-serif;color:var(--white);width:140px}
.article-more{position:absolute;left:281px;font:700 8px "Montserrat",sans-serif;color:var(--footer-head)}
.divider{position:absolute;left:281px;top:143px;width:146px;height:1px;background:#444}
.sitemap{position:absolute;top:48px;font:400 8px/15px "Montserrat",sans-serif;color:var(--footer-text)}
.footer-base{position:absolute;left:0;top:1157px;width:763px;height:43px;background:var(--footer-base)}
.copyright{position:absolute;left:90px;top:16px;font:400 8px "Montserrat",sans-serif;color:#aaa}
.social-dots{position:absolute;left:588px;top:12px}
</style>
</head>
<body>

<header class="site-header">
  <div class="brand">Morvik</div>
  <nav class="main-nav">
    <span style="left:372px">Home</span>
    <span style="left:420px">Tour</span>
    <span style="left:466px">Pricing</span>
    <span style="left:524px">Contact</span>
    <span class="login" style="left:576px"><svg width="7" height="8" viewBox="0 0 7 8"><rect x="0.5" y="3.5" width="6" height="4.5" fill="#1f6fb8"/><path d="M1.8 3.6V2.2a1.7 1.7 0 0 1 3.4 0v1.4" fill="none" stroke="#1f6fb8" stroke-width="1.1"/></svg>Login</span>
    <span class="register" style="left:624px"><svg width="8" height="8" viewBox="0 0 8 8"><circle cx="4" cy="4" r="4" fill="#f07a22"/><path d="M4 2v4M2 4h4" stroke="#fff" stroke-width="1.2"/></svg>Register</span>
  </nav>
</header>

<section class="hero">
  <div class="hero-monitor" role="img" aria-label="Desktop monitor showing a pile of fresh fruit and vegetables"></div>
  <h1 class="hero-title">The last eCommerce solution you'll need</h1>
  <p class="hero-copy">Accept orders from your website, Facelink, Pinmark, a Pagemill blog, your Morvik store, eMail, Chirper, Callwave, SMS, a printed broshures, magazines, radio and TV. Zero programming, total design freedom.</p>
  <div class="btn-start">It's free! Start here →</div>
</section>

<section class="promo">
  <div class="promo-model" role="img" aria-label="Smiling woman in an orange jacket in a bright interior"></div>
  <h2 class="promo-title">Get ready to sell in <em>45 seconds</em></h2>
  <p class="promo-copy">100 percent sales: zero programming. 45 seconds to get started. Sell from your website, Facelink, Pinmark, a Pagemill blog or your Morvik store. It's simple. Join the Morvik revolution.</p>
  <div class="partners" style="top:226px"><span>Paywell</span><span>Certivo</span><span>Insolva</span><span>Trexa</span><span>Parcelo</span><span>Swiftly</span></div>
  <div class="partners" style="top:253px;left:99px"><span>Fleetex</span><span>Ledgerly</span><span>Facelink</span><span>Pagemill</span><span>Vidstream</span><span>Pinmark</span></div>
</section>

<h2 class="feature-title blue">Simple solutions, powerful results</h2>
<p class="feature-copy" style="left:89px;width:250px">Now you can have kick-ass eCommerce with zero programming. Start selling from anywhere you want in under 60 seconds.</p>
<div class="magic">IT'S ALMOST LIKE MAGIC.</div>

<div class="card-label" style="left:89px">THIS WORKS:</div>
<div class="card-label" style="left:168px">AND THIS:</div>
<div class="card-label" style="left:247px">AND THIS:</div>

<div class="product-card" style="left:89px">
  <div class="product-photo" role="img" aria-label="Oranges" style="background:radial-gradient(circle,#f7a21c 40%,#fff 75%)"></div>
  <div class="product-name">Oranges<br>$0.10 each</div>
  <div class="buy-now">Buy Now</div>
</div>
<div class="product-card" style="left:168px">
  <div class="product-photo" role="img" aria-label="Bananas" style="background:radial-gradient(ellipse,#f2d21e 40%,#fff 75%)"></div>
  <div class="product-name">Bananas<br>$0.10 each</div>
  <div class="buy-now">Buy Now</div>
</div>
<div class="product-card" style="left:247px">
  <div class="product-photo" role="img" aria-label="Broccoli" style="background:radial-gradient(circle,#3f8a2a 40%,#fff 75%)"></div>
  <div class="product-name">Broccoli<br>$0.10 each</div>
  <div class="buy-now">Buy Now</div>
</div>

<p class="more-links">Of course you can also include <b>buy now links</b><br>directly in any text on any page.</p>

<h2 class="feature-title dark">Watch our video</h2>
<p class="feature-copy" style="left:442px;width:232px">Accept payments and orders, manage products, look after shipping and taxes, customers, members, re-sellers, affiliate partners, offer discounts, gift vouchers and much, much more.</p>
<div class="video" role="img" aria-label="Video preview of the Morvik sign-up page">
  <svg class="video-play" width="44" height="44" viewBox="0 0 44 44"><circle cx="22" cy="22" r="22" fill="#e8221b"/><path d="M17 13l14 9-14 9z" fill="#fff"/></svg>
  <div class="video-bar"></div>
</div>

<footer class="site-footer">
  <h3 class="footer-head" style="left:89px">Newsletter Signup</h3>
  <p class="footer-text" style="left:89px;top:48px;width:140px">Sign-up to be the first to know about out latest news and offers.</p>
  <div class="field" style="top:89px">Full name:</div>
  <div class="field" style="top:115px">Email address:</div>
  <div class="btn-submit">Submit</div>
  <div class="share" style="left:89px">+1</div>
  <div class="share" style="left:112px">Share</div>
  <div class="share" style="left:152px">Post</div>
  <div class="share" style="left:189px">Like 334</div>

  <h3 class="footer-head" style="left:281px">Latest Articles</h3>
  <div class="article-title" style="top:50px">Selling via Hearthsite websites made easy</div>
  <p class="footer-text" style="left:281px;top:75px;width:135px;line-height:11px">Watch this video to find out how to add powerful eCommerce functions to Hearthsite.com websites - with your..</p>
  <div class="article-more" style="top:125px">More..</div>
  <div class="divider"></div>
  <div class="article-title" style="top:155px">Morvik Mark 2 a big upgrade</div>
  <p class="footer-text" style="left:281px;top:170px;width:135px;line-height:11px">Morvik Mark 2 has been released and adds many new and exciting features. Find out more here....</p>
  <div class="article-more" style="top:209px">More..</div>

  <h3 class="footer-head" style="left:479px">Site Map</h3>
  <div class="sitemap" style="left:480px">Home<br>For Designers<br>Fundraisers<br>For Marketers<br>About Us<br>Affiliate marketing materials<br>Become an Affiliate<br>Blog<br>Contact<br>Get a free account</div>
  <div class="sitemap" style="left:616px">Partners<br>Pricing<br>Privacy<br>Terms<br>Tutorials<br>Tour<br>Home<br>Fresh Oranges<br>Tour</div>
</footer>

<div class="footer-base">
  <div class="copyright">Copyright © 2013 Morvik. All Rights Reserved.</div>
  <svg class="social-dots" width="86" height="20" viewBox="0 0 86 20">
    <circle cx="10" cy="10" r="9" fill="#444"/>
    <circle cx="32" cy="10" r="9" fill="#444"/>
    <circle cx="54" cy="10" r="9" fill="#444"/>
    <circle cx="76" cy="10" r="9" fill="#444"/>
  </svg>
</div>

</body>
</html>
```